Lantern Harbor CD design

I need a CD cover & sleeve design for an upcoming February 2014 CD release event (at a music store). This is a collection of original songs written and sung by yours truly. Many songs are inspired by my ancestors, although there are a few songs that are just about life and love. We are all a product of our ancestry, and we carry this history in our hearts whether we think it influences us or not. This is my first CD although I've been singing and performing for over 30 years, and this body of work is where I'm at now musically and creatively. I'm proud of the effort I've made and want to present myself as someone who is real and genuine. My design style tends towards simple, clean, uncluttered lines, sans serif type faces. No loud or saturated colors please, no reds or pinks. I love the blues & greens. I have a sepia image in my head, but maybe because I've been looking at old photos of my grandparents as inspiration for the last 6 months...!

I am including two shots of me, and some old photos that could be used as a design element, but not mandatory. I wanted you to have some choices... I also have a lot of CD liner notes, but am willing to edit if I need to. This would need to be in 4 color with a sleeve that flaps open, and a lift of something similar for CD imprint. Sorry about the tight deadline, I have to get a print run done before the launch and that lead time is ridiculously tight. If you want an mp3 sample of one song I am happy to forward to give you an idea of my sound, it might help to inspire if you're a music person :-) just let me know at marenvoltatquillmaildotcom

Update for inside text: Cover photo by Arthur Penwick, others photos taken by Maren Volt.

Target Market(s)

Anyone who likes original singer / songwriter music, fellow music lovers, audience members after a performance. My influence is only in the northeast US thus far.

Industry/Entity Type

Store

Requirements
Must have
• Title of CD: Lantern Harbor

Name: Maren Volt

lower left back corner - leave 1-1/4"x1/2" room in design on back cover for UPC barcode
Nice to have
• A lighter touch, artistic vibe, softer painterly approach, Don't mind the blue / green spectrum, or a sepia toned feel. Some music folks feedback has inspired me to update this: I need o have my face on the cover! the b&w shot is a little better. And it would be nice to incorporate both sets of ancestor pictures in some way. (The faded grandma and young boy and the couple with flowers that I am holding).
Song list on the back is helpful, too.
Should not have
• No loud, saturated colors, no reds or pinks please.

```html
<!DOCTYPE html>
<html lang="en">
<head>
<meta charset="utf-8">
<title>Lantern Harbor – Back Cover</title>
<link href="https://fonts.googleapis.com/css2?family=Arimo&family=Roboto+Condensed&display=swap" rel="stylesheet">
<style>
  :root {
    --page: #ffffff;
    --panel: #3d3634;
    --frame: #bdb9b6;
    --text-light: #c9c6c3;
    --spine-text: #2f2f2f;
    --photo-dark: #2a2827;
    --photo-light: #9a9794;
  }
  html, body {
    margin: 0;
    padding: 0;
    overflow: hidden;
    background: var(--page);
  }
  .canvas {
    position: relative;
    width: 1200px;
    height: 993px;
    background: var(--page);
    overflow: hidden;
    font-family: "Arimo", Arial, sans-serif;
  }
  .back-panel {
    position: absolute;
    left: 162px;
    top: 97px;
    width: 876px;
    height: 795px;
    background: var(--panel);
  }
  .inner-frame {
    position: absolute;
    left: 186px;
    top: 141px;
    width: 832px;
    height: 698px;
    border: 4px solid var(--frame);
  }
  .spine-label {
    position: absolute;
    font-size: 22px;
    color: var(--spine-text);
    white-space: nowrap;
    letter-spacing: 0.4px;
  }
  .spine-left {
    left: 140px;
    top: 521px;
    transform: translate(-50%, -50%) rotate(-90deg);
  }
  .spine-right {
    left: 1059px;
    top: 499px;
    transform: translate(-50%, -50%) rotate(90deg);
  }
  .liner-notes {
    position: absolute;
    left: 228px;
    top: 171px;
    margin: 0;
    font-size: 22.3px;
    line-height: 29.7px;
    color: var(--text-light);
    transform: scaleX(1.1);
    transform-origin: left top;
  }
  .liner-notes span { display: block; white-space: nowrap; }
  .sign-off {
    position: absolute;
    left: 804px;
    top: 524px;
    margin: 0;
    font-size: 53px;
    line-height: 1;
    color: var(--text-light);
  }
  .photo-frame {
    position: absolute;
    left: 188px;
    top: 568px;
    width: 372px;
    height: 268px;
    border: 4px solid var(--frame);
  }
  .photo-fill {
    width: 100%;
    height: 100%;
    background: linear-gradient(180deg, var(--photo-light) 0%, #6f6c69 45%, var(--photo-dark) 100%);
  }
  .credits {
    position: absolute;
    left: 578px;
    top: 608px;
    width: 440px;
    margin: 0;
    text-align: center;
    font-family: "Roboto Condensed", "Arial Narrow", sans-serif;
    font-size: 16.5px;
    line-height: 26.6px;
    color: var(--text-light);
    transform: scaleX(0.88);
    transform-origin: center top;
  }
  .credits span { display: block; white-space: nowrap; }
  .credits .copyright { margin-top: 27px; }
</style>
</head>
<body>
<div class="canvas">
  <div class="spine-label spine-left">Lantern Harbor by Maren Volt</div>
  <div class="spine-label spine-right">Lantern Harbor by Maren Volt</div>

  <div class="back-panel"></div>
  <div class="inner-frame"></div>

  <p class="liner-notes">
    <span>Like most folks in this country, I am the product of mixed ancestry.</span>
    <span>My lineage is from Russian and Romanian Jews, and early American</span>
    <span>English &amp; Scottish settlers who made their way south.&nbsp; The hardships</span>
    <span>that both sets of my grandparents dealt with are difficult to compare</span>
    <span>to what we experience now.&nbsp; All of their history and this lineage have</span>
    <span>shaped me.&nbsp; It was only a few years ago that I decided to start</span>
    <span>songwriting again after seeing the last of four children out the door</span>
    <span>into their own lives.&nbsp; Singing is something I’ve always done, having</span>
    <span>grown up with a grandmother, mother and sister who sang and</span>
    <span>played piano.&nbsp; I thank those talented women for their encouragement.</span>
    <span>Guitar playing provides the inspiration for me to write, one I hope</span>
    <span>continues until I can’t move my fingers anymore.</span>
  </p>
  <p class="sign-off">Amen.</p>

  <div class="photo-frame">
    <div class="photo-fill" role="img" aria-label="Black and white photograph of a small town main street with shops, a steeple and parked vintage cars"></div>
  </div>

  <p class="credits">
    <span>Recorded at Tin Cup Music, Alderbrook, CT</span>
    <span>www.tincupmusic.com, and at Dan Welles Studio in Westbury, CT.</span>
    <span>Mixed by Dan Welles, Westbury,</span>
    <span>CT &amp; Millbrook, IL</span>
    <span>Photography by Arthur Penwick</span>
    <span>Sweet June written by Ed Marsh &amp; Otto Lind 1928</span>
    <span class="copyright">© Original lyrics and music by Maren Volt 2013</span>
  </p>
</div>
</body>
</html>
```